Website design for commercial and residential security company

we're looking to see some new designs for an established company with no website.

homepage and one inner page

here is a link to the homepage content, sitemap, logo and more.
https://files.brontavel.net/share/7QxmPzLrTw2vNkdJhYcsa9eFgbUoiVwRn?view=open

call to action should be Request A Quote

if you have any questions please send them to us asap

thank you

1 page

Sans Serif

```html
<!DOCTYPE html>
<html lang="en">
<head>
<meta charset="utf-8">
<title>Beacon Ridge Security</title>
<link rel="stylesheet" href="https://fonts.googleapis.com/css2?family=Montserrat:ital,wght@0,400;0,500;0,600;0,700;0,800;1,400;1,500&family=Roboto:wght@300;400&display=swap">
<style>
:root{
  --orange:#ff7f00;
  --dark:#232323;
  --white:#ffffff;
  --green:#22c922;
  --green-btn:#00c400;
  --navy-top:#0e2253;
  --navy-row-a:#112a62;
  --navy-row-b:#0b1f4f;
  --navy-price:#04194a;
  --muted:#e8e8e8;
}
*{margin:0;padding:0;box-sizing:border-box}
html,body{width:1200px;height:3000px;overflow:hidden;background:var(--dark)}
body{font-family:"Montserrat",sans-serif;color:var(--white)}
.page{position:relative;width:1200px;height:3000px;background:var(--dark)}
.abs{position:absolute}

/* hero */
.hero{left:0;top:0;width:1200px;height:459px;background:linear-gradient(160deg,#1d2b66 0%,#27326e 35%,#3b3f6e 60%,#6a4f5a 85%,#8a5c4a 100%)}
.hero-camera{left:792px;top:0;width:408px;height:459px;background:radial-gradient(circle at 55% 40%,#c9ced6 0%,#6b717c 30%,#23262c 60%,#111216 100%)}
.brand{left:225px;top:36px;display:flex;align-items:center;gap:8px;font-weight:800;font-size:16px;letter-spacing:.5px}
.brand-dot{width:12px;height:12px;background:var(--white);border-radius:50%}
.nav{top:40px;font-size:12px;font-weight:700}
.hero-title{left:222px;top:130px;width:420px;font-size:34px;font-weight:700;line-height:45px}
.hero-sub{left:222px;top:221px;width:420px;font-size:23px;line-height:33px;font-weight:500}
.btn-quote{left:222px;top:337px;width:137px;height:37px;background:var(--orange);color:var(--white);font-size:10px;font-weight:700;display:flex;align-items:center;justify-content:center;letter-spacing:.3px}

.band{left:0;top:459px;width:1200px;height:125px;background:var(--orange)}
.band p{position:absolute;left:222px;top:19px;width:720px;font-style:italic;font-size:16.5px;line-height:28px}

/* solution blocks */
.sec-title{color:var(--orange);font-weight:800;font-size:23px;line-height:33px}
.lead{font-style:italic;font-weight:500;font-size:17px;line-height:24px}
.body-text{font-size:12.2px;line-height:17px}
.photo-commercial{left:613px;top:624px;width:362px;height:306px;background:linear-gradient(180deg,#7fa6d6 0%,#cfdcec 55%,#5a7fae 100%)}
.photo-residential{left:222px;top:930px;width:391px;height:325px;background:linear-gradient(180deg,#d7dde3 0%,#9aaab0 40%,#4f6a3c 70%,#a7a59c 100%)}
.divider{left:312px;top:1306px;width:550px;height:1px;background:var(--orange)}

.lead2{font-style:italic;font-size:17.5px;line-height:28px}
.read-more{color:var(--orange);font-weight:800;font-size:15px}
.feat-icon{width:34px;height:34px}
.feat-title{font-weight:700;font-size:14px}
.feat-desc{font-size:12px;line-height:17px;width:175px}
.more{font-weight:700;font-size:14.5px;line-height:28px;width:130px}
.btn-ghost{width:82px;height:25px;border:1px solid var(--green);color:var(--green);font-size:9px;font-weight:700;display:flex;align-items:center;justify-content:center;border-radius:2px}

/* pricing */
.card{top:2140px;width:203px;height:382px;border-radius:8px;overflow:hidden;background:var(--navy-price);font-family:"Roboto",sans-serif}
.card-name{height:58px;background:var(--navy-top);color:var(--green);font-weight:300;font-size:26px;text-align:center;padding-top:18px;letter-spacing:.5px}
.card-row{height:46px;display:flex;align-items:center;justify-content:space-between;padding:0 36px 0 37px;font-size:7.5px;line-height:9px;color:#dfe6f5}
.card-row:nth-child(even){background:var(--navy-row-a)}
.card-row:nth-child(odd){background:var(--navy-row-b)}
.card-row span{width:100px}
.price{text-align:center;font-weight:300;font-size:44px;margin-top:10px;line-height:46px}
.price sup{font-size:20px;vertical-align:top;line-height:30px}
.per{text-align:center;font-size:12px;margin-top:0}
.btn-sub{margin:22px auto 0;width:126px;height:28px;border-radius:14px;background:var(--green-btn);font-size:13px;display:flex;align-items:center;justify-content:center}

/* footer */
.field{height:28px;border:1px solid var(--orange);font-size:9px;padding-left:12px;display:flex;align-items:center}
.btn-orange{background:var(--orange);font-size:9px;font-weight:700;display:flex;align-items:center;justify-content:center}
.f-head{color:var(--orange);font-weight:700;font-size:12px;top:2688px}
.f-item{font-size:9.5px;font-weight:500}
.f-label{font-size:9px;font-weight:700}
.f-box{left:748px;width:227px;border:1px solid var(--orange)}
.c-icon{width:17px;height:17px;border-radius:50%;background:var(--orange)}
.rule{left:225px;top:2938px;width:750px;height:1px;background:#6a6a6a}
.legal{font-size:9px;top:2964px}
.social{top:2958px;width:20px;height:20px;border-radius:50%;background:var(--orange)}
</style>
</head>
<body>
<div class="page">

  <header class="abs hero">
    <div class="abs hero-camera" role="img" aria-label="Close-up photo of a dome security camera"></div>
    <div class="abs brand"><span class="brand-dot"></span>BEACON RIDGE</div>
    <nav>
      <span class="abs nav" style="left:386px">Home</span>
      <span class="abs nav" style="left:453px">About</span>
      <span class="abs nav" style="left:521px">Solutions</span>
      <span class="abs nav" style="left:608px">Resources</span>
      <span class="abs nav" style="left:700px">Contact</span>
    </nav>
    <h1 class="abs hero-title">We ensure security with smart tools</h1>
    <p class="abs hero-sub">Providing comprehensive security audio/video, and automation with top notch customer service.</p>
    <a class="abs btn-quote">GET A QUOTE</a>
  </header>

  <section class="abs band">
    <p>The graded security measures from Beacon Ridge Security ensure the safety of both residential and commercial property. We provide a wide range of Residential and Commercial Security Solutions.</p>
  </section>

  <section class="solutions-intro">
    <h2 class="abs sec-title" style="left:221px;top:678px">Commercial Solutions</h2>
    <p class="abs lead" style="left:221px;top:719px;width:370px">Protect assets and security of your business with Exceptional Commercial Security Installation</p>
    <p class="abs body-text" style="left:221px;top:804px;width:370px">People's safety is our top priority. This includes ensuring that the security system built at your commercial property is configured accurately. Further, it will protect against intruders, burglaries, and holdups.</p>
    <div class="abs photo-commercial" role="img" aria-label="Photo of security cameras mounted on a pole inside a glass building"></div>

    <div class="abs photo-residential" role="img" aria-label="Photo of an outdoor camera watching a residential house"></div>
    <h2 class="abs sec-title" style="left:638px;top:969px;width:300px">Residential Security Solutions</h2>
    <p class="abs lead" style="left:638px;top:1041px;width:320px">Consider a home surveillance device that would do more for you and your family than you ever imagined.</p>
    <p class="abs body-text" style="left:638px;top:1127px;width:330px">Beacon Ridge Security is your trustable security provider. Also, as certified professionals carry out the installation, you have everything under control. A home is being securely watched from various points, with cameras capable of tracking any intruder's path.</p>
  </section>

  <div class="abs divider"></div>

  <section class="commercial-detail">
    <h2 class="abs sec-title" style="left:223px;top:1346px">Commercial Solutions</h2>
    <p class="abs lead2" style="left:223px;top:1381px;width:400px">We will help secure your company outside of the realm of conventional monitoring technologies. we take a customised and comprehensive approach to defence.</p>
    <p class="abs body-text" style="left:223px;top:1514px;width:395px">Flooding, smoke, power outages, temperature fluctuations, and other factors will all be tracked. So, you can take prompt steps before you experience damage. But, it all comes down to internal and external security measures. We can combine low-light cameras smoke and temperature monitoring, noise control, and physical surveillance into a 24/7 commercial security solution.</p>
    <span class="abs read-more" style="left:223px;top:1629px">Read More</span>

    <svg class="abs feat-icon" style="left:650px;top:1352px" viewBox="0 0 34 34" fill="none" stroke="var(--green)" stroke-width="1.6"><rect x="3" y="8" width="22" height="9" transform="rotate(12 14 12)"/><path d="M25 12l6-2v8l-6-1M10 20v6H4M10 26h4"/></svg>
    <div class="abs feat-title" style="left:650px;top:1402px">CCTV Cameras</div>
    <div class="abs feat-desc" style="left:650px;top:1426px">With facial recognition technology.</div>

    <svg class="abs feat-icon" style="left:845px;top:1352px" viewBox="0 0 34 34" fill="none" stroke="var(--green)" stroke-width="1.6"><rect x="4" y="4" width="14" height="26" rx="2"/><path d="M8 9h6M8 14h6M22 12a6 6 0 0 1 0 10M26 9a10 10 0 0 1 0 16"/></svg>
    <div class="abs feat-title" style="left:845px;top:1402px">Detectors</div>
    <div class="abs feat-desc" style="left:845px;top:1426px;width:140px">Detect's and prevent's intrusion.</div>

    <svg class="abs feat-icon" style="left:650px;top:1511px" viewBox="0 0 34 34" fill="none" stroke="var(--green)" stroke-width="1.6"><circle cx="15" cy="15" r="12"/><path d="M9 15v0M12 11v8M15 8v14M18 11v8M21 14v2"/><circle cx="24" cy="24" r="5"/></svg>
    <div class="abs feat-title" style="left:650px;top:1562px">Audio / Video</div>
    <div class="abs feat-desc" style="left:650px;top:1586px;width:150px">Live recording Solutions for your property.</div>

    <div class="abs more" style="left:847px;top:1514px">For More details on features we offer.</div>
    <a class="abs btn-ghost" style="left:847px;top:1619px">Get Info</a>
  </section>

  <section class="residential-detail">
    <h2 class="abs sec-title" style="left:222px;top:1715px">Residential Security Solutions</h2>
    <p class="abs lead2" style="left:222px;top:1747px;width:400px">Consider a home surveillance device that would do more for you and your family than you ever imagined.</p>
    <p class="abs body-text" style="left:222px;top:1845px;width:395px">Beacon Ridge Security is your trustable security provider. Also, as certified professionals carry out the installation, you have everything under control. Your home is being securely watched from various points, with cameras capable of tracking any intruder's path. Specifically, we offer Residential Intrusion Detection Security Systems, Residential Alarm, Residential Network Wi-Fi, CCTVs and residential home automation.</p>
    <span class="abs read-more" style="left:222px;top:1990px">Read More</span>

    <svg class="abs feat-icon" style="left:650px;top:1723px" viewBox="0 0 34 34" fill="none" stroke="var(--green)" stroke-width="1.6"><circle cx="17" cy="17" r="15"/><path d="M9 15a11 11 0 0 1 16 0M12 18a7 7 0 0 1 10 0M15 21a3 3 0 0 1 4 0"/><circle cx="17" cy="24" r="1"/></svg>
    <div class="abs feat-title" style="left:650px;top:1777px">WI-FI Network</div>
    <div class="abs feat-desc" style="left:650px;top:1801px">With Residential Network Wi-Fi availability</div>

    <svg class="abs feat-icon" style="left:845px;top:1722px" viewBox="0 0 34 34" fill="none" stroke="var(--green)" stroke-width="1.6"><path d="M4 16L17 5l13 11M8 13v16h18V13"/><circle cx="17" cy="20" r="4"/><path d="M17 14v2M17 24v2M11 20h2M21 20h2"/></svg>
    <div class="abs feat-title" style="left:845px;top:1774px">Automation</div>
    <div class="abs feat-desc" style="left:845px;top:1801px;width:140px">Available with full automation systems.</div>

    <svg class="abs feat-icon" style="left:650px;top:1864px" viewBox="0 0 34 34" fill="none" stroke="var(--green)" stroke-width="1.6"><path d="M10 28v-9a7 7 0 0 1 14 0v9M6 28h22M17 4v4M6 9l3 3M28 9l-3 3M3 19h3M28 19h3"/></svg>
    <div class="abs feat-title" style="left:650px;top:1911px">Residential Alarm</div>
    <div class="abs feat-desc" style="left:650px;top:1934px">As part of Intrusion detection system.</div>

    <div class="abs more" style="left:847px;top:1870px">For More details on features we offer</div>
    <a class="abs btn-ghost" style="left:846px;top:1979px">Get Info</a>
  </section>

  <section class="pricing">
    <div class="abs card" style="left:260px">
      <div class="card-name">BASIC</div>
      <div class="card-rows">
        <div class="card-row"><span>Lorem ipsum dolor sit amet, consectetuer</span><svg width="14" height="12" viewBox="0 0 14 12"><path d="M1 6l4 4 8-9" stroke="var(--green)" stroke-width="2.4" fill="none"/></svg></div>
        <div class="card-row"><span>Sed diam nonummy nibh euismod tincidunt</span><svg width="14" height="12" viewBox="0 0 14 12"><path d="M1 6l4 4 8-9" stroke="var(--green)" stroke-width="2.4" fill="none"/></svg></div>
        <div class="card-row"><span>Duis autem vel eum iriure dolor in hendrerit</span><svg width="12" height="12" viewBox="0 0 12 12"><path d="M2 2l8 8M10 2l-8 8" stroke="var(--green)" stroke-width="2.4"/></svg></div>
        <div class="card-row"><span>Quis nostrud exerci tation ullamcorper suscipit lobortis</span><svg width="12" height="12" viewBox="0 0 12 12"><path d="M2 2l8 8M10 2l-8 8" stroke="var(--green)" stroke-width="2.4"/></svg></div>
      </div>
      <div class="price"><sup>$</sup>4.99</div>
      <div class="per">PER MONTH</div>
      <div class="btn-sub">SUBSCRIBE</div>
    </div>
    <div class="abs card" style="left:499px">
      <div class="card-name">STANDARD</div>
      <div class="card-rows">
        <div class="card-row"><span>Lorem ipsum dolor sit amet, consectetuer</span><svg width="14" height="12" viewBox="0 0 14 12"><path d="M1 6l4 4 8-9" stroke="var(--green)" stroke-width="2.4" fill="none"/></svg></div>
        <div class="card-row"><span>Sed diam nonummy nibh euismod tincidunt</span><svg width="14" height="12" viewBox="0 0 14 12"><path d="M1 6l4 4 8-9" stroke="var(--green)" stroke-width="2.4" fill="none"/></svg></div>
        <div class="card-row"><span>Duis autem vel eum iriure dolor in hendrerit</span><svg width="14" height="12" viewBox="0 0 14 12"><path d="M1 6l4 4 8-9" stroke="var(--green)" stroke-width="2.4" fill="none"/></svg></div>
        <div class="card-row"><span>Quis nostrud exerci tation ullamcorper suscipit lobortis</span><svg width="12" height="12" viewBox="0 0 12 12"><path d="M2 2l8 8M10 2l-8 8" stroke="var(--green)" stroke-width="2.4"/></svg></div>
      </div>
      <div class="price"><sup>$</sup>14.99</div>
      <div class="per">PER MONTH</div>
      <div class="btn-sub">SUBSCRIBE</div>
    </div>
    <div class="abs card" style="left:737px">
      <div class="card-name">PREMIUM</div>
      <div class="card-rows">
        <div class="card-row"><span>Lorem ipsum dolor sit amet, consectetuer</span><svg width="14" height="12" viewBox="0 0 14 12"><path d="M1 6l4 4 8-9" stroke="var(--green)" stroke-width="2.4" fill="none"/></svg></div>
        <div class="card-row"><span>Sed diam nonummy nibh euismod tincidunt</span><svg width="14" height="12" viewBox="0 0 14 12"><path d="M1 6l4 4 8-9" stroke="var(--green)" stroke-width="2.4" fill="none"/></svg></div>
        <div class="card-row"><span>Duis autem vel eum iriure dolor in hendrerit</span><svg width="14" height="12" viewBox="0 0 14 12"><path d="M1 6l4 4 8-9" stroke="var(--green)" stroke-width="2.4" fill="none"/></svg></div>
        <div class="card-row"><span>Quis nostrud exerci tation ullamcorper suscipit lobortis</span><svg width="14" height="12" viewBox="0 0 14 12"><path d="M1 6l4 4 8-9" stroke="var(--green)" stroke-width="2.4" fill="none"/></svg></div>
      </div>
      <div class="price"><sup>$</sup>24.99</div>
      <div class="per">PER MONTH</div>
      <div class="btn-sub">SUBSCRIBE</div>
    </div>
  </section>

  <footer>
    <div class="abs field" style="left:225px;top:2619px;width:227px">Name</div>
    <div class="abs field" style="left:486px;top:2619px;width:227px">E - Mail</div>
    <div class="abs btn-orange" style="left:748px;top:2619px;width:227px;height:28px">SUBSCRIBE</div>

    <div class="abs f-head" style="left:254px">Contact Us</div>
    <div class="abs c-icon" style="left:226px;top:2713px"></div>
    <div class="abs f-item" style="left:255px;top:2716px">+ xxx-xxx-xxxx</div>
    <div class="abs c-icon" style="left:226px;top:2742px"></div>
    <div class="abs f-item" style="left:255px;top:2745px">info@beaconridge.example</div>
    <div class="abs c-icon" style="left:226px;top:2773px"></div>
    <div class="abs f-item" style="left:255px;top:2776px;line-height:18px">Location to be stated by<br>Client data available.</div>

    <div class="abs f-head" style="left:431px">Smart Tools</div>
    <div class="abs f-item" style="left:432px;top:2716px">CCTV Camers</div>
    <div class="abs f-item" style="left:432px;top:2741px">Burgler Alarms</div>
    <div class="abs f-item" style="left:432px;top:2765px">Intruder Detection</div>
    <div class="abs f-item" style="left:432px;top:2790px">Home Automation</div>
    <div class="abs f-item" style="left:432px;top:2814px">House Alarm</div>
    <div class="abs f-item" style="left:432px;top:2839px">Audio / Video</div>
    <div class="abs f-item" style="left:432px;top:2863px;color:var(--orange);font-weight:700">Learn More</div>

    <div class="abs f-head" style="left:585px">Other links</div>
    <div class="abs f-item" style="left:586px;top:2716px">About Us</div>
    <div class="abs f-item" style="left:586px;top:2748px">Resources</div>
    <div class="abs f-item" style="left:586px;top:2779px">Solutions</div>
    <div class="abs f-item" style="left:586px;top:2811px">Contact</div>

    <div class="abs f-head" style="left:748px">Get In Touch</div>
    <div class="abs f-label" style="left:697px;top:2712px">Name</div>
    <div class="abs f-box" style="top:2714px;height:27px"></div>
    <div class="abs f-label" style="left:697px;top:2757px">E - Mail</div>
    <div class="abs f-box" style="top:2759px;height:27px"></div>
    <div class="abs f-label" style="left:697px;top:2803px">Message</div>
    <div class="abs f-box" style="top:2805px;height:61px"></div>
    <div class="abs btn-orange" style="left:748px;top:2887px;width:82px;height:24px;font-size:8px">SUBMIT</div>

    <div class="abs rule"></div>
    <div class="abs legal" style="left:223px">© 2012-2021 Beacon Ridge Security . All Rights Reserved</div>
    <div class="abs social" style="left:548px"></div>
    <div class="abs social" style="left:575px"></div>
    <div class="abs social" style="left:602px"></div>
    <div class="abs social" style="left:629px"></div>
    <div class="abs legal" style="left:791px">Terms and Conditions &nbsp;&nbsp;|&nbsp;&nbsp;&nbsp; Privacy Policy</div>
  </footer>

</div>
</body>
</html>
```